Business Card Design Project

I need a business card designed with these details on the front along with the logo attached on the front.

Address - 518/ 217 Wendlebury st Thornvale
Website - www.brackenhollowmasonry.com.au
Email - delwyn@brackenhollowmasonry.com.au
Fax - 1900 457 618
Mobile - 0471926038
Telephone - 1300517926
Licence number - 847263k

```html
<!DOCTYPE html>
<html lang="en">
<head>
<meta charset="utf-8">
<title>Bracken Hollow Masonry – Business Card</title>
<link rel="stylesheet" href="https://fonts.googleapis.com/css2?family=Tinos:wght@700&family=Open+Sans:wght@400;600;700&display=swap">
<style>
  :root {
    --bg: #ffffff;
    --brown: #3b1d15;
    --brown-text: #2a1610;
    --cream: #f1e4d3;
    --stone-light: #ece6df;
    --stone-mid: #d6ccc2;
    --mark: #e8e0d6;
    --ink: #2b201c;
  }
  * { box-sizing: border-box; margin: 0; padding: 0; }
  html, body { width: 1104px; height: 1200px; overflow: hidden; background: var(--bg); }
  body { position: relative; font-family: "Open Sans", Arial, sans-serif; color: var(--ink); }

  .card {
    position: absolute;
    left: 112px;
    width: 880px;
    height: 520px;
    overflow: hidden;
    box-shadow: 0 2px 10px rgba(0,0,0,0.18);
  }

  /* Front */
  .card-front { top: 60px; background: var(--brown); }
  .brand {
    position: absolute;
    left: 100px; top: 150px;
    display: flex; align-items: center; gap: 40px;
  }
  .brand-square {
    width: 130px; height: 130px;
    background: var(--cream);
  }
  .brand-name {
    font-family: "Tinos", "Times New Roman", serif;
    font-weight: 700;
    font-size: 54px;
    line-height: 1.12;
    letter-spacing: 1px;
    text-transform: uppercase;
    color: var(--cream);
  }
  .front-web {
    position: absolute;
    left: 0; right: 0; bottom: 52px;
    text-align: center;
    font-weight: 700;
    font-size: 32px;
    color: var(--cream);
  }

  /* Back */
  .card-back { top: 640px; background: var(--bg); }
  .stone-area {
    position: absolute;
    right: 0; top: 0;
    width: 400px; height: 440px;
    background: linear-gradient(160deg, var(--stone-light), var(--stone-mid));
  }
  .faint-mark {
    position: absolute;
    right: 80px; top: 60px;
    width: 240px; height: 240px;
    background: var(--mark);
    opacity: 0.8;
  }
  .write-line {
    position: absolute;
    left: 120px; width: 600px; height: 3px;
    background: var(--brown);
  }
  .write-line.first { top: 60px; }
  .write-line.second { top: 140px; }
  .contact {
    position: absolute;
    left: 40px; right: 40px; top: 232px;
    text-align: center;
    color: var(--brown-text);
  }
  .licence { font-weight: 600; font-size: 18px; margin-bottom: 8px; }
  .address { font-size: 25px; margin-bottom: 8px; }
  .numbers { font-size: 25px; margin-bottom: 8px; }
  .numbers .main-phone { font-weight: 700; font-size: 30px; }
  .email { font-size: 21px; }
  .bottom-band {
    position: absolute;
    left: 0; right: 0; bottom: 0;
    height: 80px;
    background: var(--brown);
  }
</style>
</head>
<body>
  <section class="card card-front">
    <div class="brand">
      <div class="brand-square"></div>
      <div class="brand-name">Bracken Hollow<br>Masonry</div>
    </div>
    <p class="front-web">www.brackenhollowmasonry.com.au</p>
  </section>

  <section class="card card-back">
    <div class="stone-area" role="img" aria-label="Soft sandstone texture panel"></div>
    <div class="faint-mark"></div>
    <div class="write-line first"></div>
    <div class="write-line second"></div>
    <div class="contact">
      <p class="licence">Licence number - 847263k</p>
      <p class="address">518/ 217 Wendlebury st Thornvale</p>
      <p class="numbers"><span class="main-phone">p: 1300 517 926</span> • m: 0471 926 038 • f: 1900 457 618</p>
      <p class="email">e: delwyn@brackenhollowmasonry.com.au</p>
    </div>
    <div class="bottom-band"></div>
  </section>
</body>
</html>
```